Flyer for the Lumen 2025 Conference

I am looking to produce a flyer for our upcoming conference, Lumen 2025. This is an annual conference that we plan to publicize on social media. The ideal designer will create a flyer that is eye-catching and effectively communicates the key information. Please see attached our logo, speaker photo, and flyer content.

Target Market(s)

All demographics

Industry/Entity Type

Christian

Font styles to use
Sans Serif

Requirements
Should not have
• Cross, church

```html
<!DOCTYPE html>
<html lang="en">
<head>
<meta charset="utf-8">
<title>Lumen 2025 Conference</title>
<link href="https://fonts.googleapis.com/css2?family=Lexend:wght@300;400;500;600;700&family=Montserrat:wght@800&family=Great+Vibes&display=swap" rel="stylesheet">
<style>
  :root {
    --blue-deep: #06315f;
    --blue-mid: #0b4f97;
    --blue-bright: #1b8ff0;
    --blue-sky: #29b6ff;
    --blue-button: #1a7ad9;
    --orange: #fb8a10;
    --orange-dark: #f26d05;
    --flame: #f43c1f;
    --ink: #111;
    --white: #fff;
  }
  * { box-sizing: border-box; margin: 0; padding: 0; }
  html, body { width: 944px; height: 1200px; overflow: hidden; background: var(--white); }
  body { font-family: "Lexend", sans-serif; color: var(--ink); }
  .flyer { position: relative; width: 944px; height: 1200px; overflow: hidden; background: var(--white); }

  .hero {
    position: absolute; left: 0; top: 0; width: 944px; height: 720px;
    background:
      radial-gradient(circle at 60% 55%, rgba(255,255,255,0.04) 0 300px, transparent 301px),
      radial-gradient(circle at 60% 55%, rgba(255,255,255,0.03) 0 420px, transparent 421px),
      linear-gradient(120deg, #1166c4 0%, var(--blue-mid) 35%, var(--blue-deep) 75%);
  }
  .hero-words { position: absolute; left: 0; top: 0; }

  .brand {
    position: absolute; left: 0; right: 0; top: 78px;
    display: flex; align-items: center; justify-content: center; gap: 10px;
  }
  .brand-dot { width: 16px; height: 16px; border-radius: 50%; background: var(--orange); }
  .brand-name { font-size: 44px; font-weight: 500; letter-spacing: 2px; color: var(--white); }

  .speaker-photo {
    position: absolute; left: 262px; top: 196px; width: 526px; height: 520px;
    border-radius: 180px 180px 0 0;
    background: linear-gradient(180deg, #2a5f9a 0%, #1c6fd0 55%, #1561bf 100%);
  }

  .torn-edge { position: absolute; left: 0; top: 700px; }

  .ribbon { position: absolute; left: 54px; top: 740px; }
  .ribbon-title {
    position: absolute; left: 153px; top: 742px;
    font-size: 33px; font-weight: 700; line-height: 44px; color: var(--white); letter-spacing: -0.5px;
  }

  .topic { position: absolute; left: 104px; top: 890px; width: 326px; }
  .topic-label { font-size: 23px; font-weight: 600; margin-top: 20px; line-height: 28px; }
  .topic-title { font-size: 25px; font-weight: 300; line-height: 32px; margin-bottom: 12px; }

  .app-note { position: absolute; left: 108px; top: 1014px; font-size: 16px; font-weight: 300; line-height: 21px; }

  .contact-box {
    position: absolute; left: 108px; top: 1070px; width: 187px; height: 79px;
    background: var(--blue-button); border-radius: 2px; padding: 10px 0 0 16px;
    color: var(--white); font-size: 13px; font-weight: 300; line-height: 19px;
  }
  .contact-row { display: flex; align-items: center; gap: 8px; }
  .contact-row svg { flex: none; }

  .with { position: absolute; left: 484px; top: 735px; font-family: "Great Vibes", cursive; font-size: 62px; color: var(--blue-button); }
  .speaker-name { position: absolute; left: 484px; top: 822px; font-size: 29px; font-weight: 600; letter-spacing: -0.5px; }

  .session { position: absolute; line-height: 27px; }
  .session-day { font-size: 21px; font-weight: 600; color: var(--orange); }
  .session-time { font-size: 22px; font-weight: 300; }
  .session-fri { left: 484px; top: 880px; }
  .session-sat { left: 650px; top: 952px; }
  .session-sun { left: 484px; top: 1022px; }

  .venue { position: absolute; left: 484px; top: 1108px; display: flex; gap: 8px; font-size: 13px; line-height: 15px; font-weight: 400; }

  .flame-art {
    position: absolute; left: 790px; top: 1020px; width: 154px; height: 180px;
    border-radius: 120px 0 0 0;
    background: linear-gradient(160deg, #ff5a2a 0%, var(--flame) 100%);
  }
</style>
</head>
<body>
<main class="flyer">
  <section class="hero">
    <div class="speaker-photo" role="img" aria-label="Portrait photo of the speaker in a blue blazer"></div>
    <svg class="hero-words" width="944" height="720" viewBox="0 0 944 720">
      <defs>
        <linearGradient id="word-fill" x1="0" y1="1" x2="0" y2="0">
          <stop offset="0" stop-color="#2aa6ff"/>
          <stop offset="1" stop-color="#1d82e8"/>
        </linearGradient>
      </defs>
      <text transform="translate(229 680) rotate(-90)" font-family="Montserrat, sans-serif" font-weight="800" font-size="188" fill="url(#word-fill)" textLength="630" lengthAdjust="spacingAndGlyphs">LUMEN</text>
      <text transform="translate(890 676) rotate(-90)" font-family="Montserrat, sans-serif" font-weight="800" font-size="182" fill="url(#word-fill)" textLength="370" lengthAdjust="spacingAndGlyphs">2025</text>
    </svg>
    <div class="brand">
      <span class="brand-dot"></span>
      <span class="brand-name">VERAVOX</span>
    </div>
  </section>

  <svg class="torn-edge" width="944" height="30" viewBox="0 0 944 30">
    <path d="M0 0 H944 V19 L930 21 L912 18 L896 22 L870 19 L848 23 L820 20 L796 22 L770 19 L742 24 L716 20 L690 22 L660 19 L630 23 L600 20 L572 22 L540 19 L510 23 L480 20 L452 21 L420 19 L392 23 L360 20 L330 22 L300 19 L270 24 L240 20 L212 22 L180 19 L150 23 L120 20 L92 22 L62 18 L36 23 L14 19 L0 21 Z" fill="#0d5db2"/>
  </svg>

  <svg class="ribbon" width="430" height="152" viewBox="0 0 430 152">
    <path d="M430 0 L402 60 Q380 108 340 116 L22 116 Q8 116 0 152 Q-4 130 20 80 L40 30 Q48 12 68 12 L400 12 Z" fill="var(--orange)"/>
    <path d="M430 0 L400 12 L380 80 Q400 94 388 112 Q410 96 418 60 Z" fill="var(--orange-dark)"/>
    <path d="M40 30 Q60 14 70 40 L30 116 L0 152 Q8 112 22 90 Z" fill="#ff9e1f"/>
  </svg>
  <div class="ribbon-title">Prophetic<br>Conference</div>

  <div class="topic">
    <svg width="326" height="10" viewBox="0 0 326 10"><path d="M3 5 H326" stroke="#222" stroke-width="1"/><path d="M3 0 L4.2 3.8 L8 5 L4.2 6.2 L3 10 L1.8 6.2 -2 5 1.8 3.8Z" fill="var(--blue-button)"/></svg>
    <p class="topic-label">Topic:</p>
    <p class="topic-title">The Voice Of The Lord</p>
    <svg width="326" height="10" viewBox="0 0 326 10"><path d="M0 5 H320" stroke="#222" stroke-width="1"/><path d="M320 0 L321.2 3.8 L325 5 L321.2 6.2 L320 10 L318.8 6.2 L315 5 L318.8 3.8Z" fill="var(--blue-button)"/></svg>
  </div>

  <p class="app-note">Download the Veravox App<br>to stay updated on the event</p>

  <div class="contact-box">
    <div class="contact-row">
      <svg width="10" height="10" viewBox="0 0 24 24"><path d="M6.6 10.8a15 15 0 0 0 6.6 6.6l2.2-2.2a1 1 0 0 1 1-.25 11.4 11.4 0 0 0 3.6.57 1 1 0 0 1 1 1V20a1 1 0 0 1-1 1A17 17 0 0 1 3 4a1 1 0 0 1 1-1h3.5a1 1 0 0 1 1 1c0 1.25.2 2.45.57 3.6a1 1 0 0 1-.25 1z" fill="#fff"/></svg>
      <span>555 014 2290</span>
    </div>
    <div class="contact-row">
      <svg width="10" height="10" viewBox="0 0 24 24"><path d="M2 5h20v14H2z" fill="#fff"/><path d="M2 5l10 8 10-8" fill="none" stroke="var(--blue-button)" stroke-width="2"/></svg>
      <span>hello@veravox.org</span>
    </div>
    <div class="contact-row">
      <svg width="10" height="10" viewBox="0 0 24 24"><path d="M4 2l16 10-7 1.5 4 8-3 1.5-4-8L4 20z" fill="#fff"/></svg>
      <span>www.veravox.org</span>
    </div>
  </div>

  <p class="with">with</p>
  <h2 class="speaker-name">Prophet Elias Marlow</h2>

  <div class="session session-fri"><p class="session-day">Fri, Dec 26th,</p><p class="session-time">6:30PM - 9:00PM</p></div>
  <div class="session session-sat"><p class="session-day">Sat, Dec 27th,</p><p class="session-time">5:30PM &nbsp;- 8:00PM</p></div>
  <div class="session session-sun"><p class="session-day">Sun, Dec 29th,</p><p class="session-time">4:30PM - 7:00PM</p></div>

  <div class="venue">
    <svg width="10" height="13" viewBox="0 0 24 32"><path d="M12 0a11 11 0 0 0-11 11c0 8 11 21 11 21s11-13 11-21A11 11 0 0 0 12 0zm0 15a4 4 0 1 1 0-8 4 4 0 0 1 0 8z" fill="#111"/></svg>
    <p>The Harborview Performing<br>Arts Center, 120 Lantern<br>Street Fairhaven, Maine 04011</p>
  </div>

  <div class="flame-art" role="img" aria-label="Decorative red flame illustration"></div>
</main>
</body>
</html>
```